Young, dynamic furniture company needs a new business card design

We require a new business card design for our modern furniture company which supplies furniture and appliances to the property and development market.
Birchlane Furnishing has become one of the leading furniture & appliance suppliers to the property market withing London. With over 10 years experience, we have increased our business to supply not only private landlords and managing agents, but also property developers, housing associations and local councils.
We offer not only a complete range of furniture which includes beds, wardrobes, dining sets and sofas, but also a high quality, full delivery and assembly service to help you with all our furnishing needs.

Target Market(s)

Private landlords, estate agents, letting agents, property management companies

Industry/Entity Type

Business

Contact Information for Business Card

Name,
Title,
Address,
Mobile,
Telephone,
Fax, Website, email address

Font styles to use
Sans Serif

Colors
3176b5
0555a3
85abd2
cfdeed

Requirements
Must have
• All the above information for each of our staff, along with our logo

```html
<!DOCTYPE html>
<html lang="en">
<head>
<meta charset="utf-8">
<title>Birchlane Furnishing – Business Card</title>
<link href="https://fonts.googleapis.com/css2?family=Open+Sans:wght@400;600;700;800&display=swap" rel="stylesheet">
<style>
  :root {
    --blue-mid: #3176b5;
    --blue-deep: #0555a3;
    --blue-soft: #85abd2;
    --blue-pale: #cfdeed;
    --ink: #0a0a0a;
    --paper: #ffffff;
    --shade: #e2e2e2;
    --backdrop: #ececec;
  }
  html, body {
    margin: 0;
    padding: 0;
    width: 1200px;
    height: 1200px;
    overflow: hidden;
    background: var(--backdrop);
    font-family: "Open Sans", Arial, sans-serif;
  }
  .canvas { position: relative; width: 1200px; height: 1200px; }
  .card {
    position: absolute;
    left: 160px;
    width: 880px;
    height: 518px;
    box-shadow: 0 6px 18px rgba(0,0,0,0.12);
    background: var(--paper);
    overflow: hidden;
  }
  .card--front { top: 45px; }
  .card--back { top: 637px; }
  .card svg { display: block; width: 100%; height: 100%; }
  .brand-name { font-weight: 700; font-size: 26px; fill: var(--ink); letter-spacing: 0.5px; }
  .brand-tagline { font-weight: 400; font-size: 14px; fill: var(--ink); letter-spacing: 0.5px; }
  .company-line { font-weight: 800; font-size: 18px; fill: var(--paper); }
  .address-line { font-weight: 400; font-size: 16px; fill: var(--paper); }
  .contact-line { font-weight: 400; font-size: 16px; fill: var(--paper); }
  .person-name { font-weight: 800; font-size: 34px; fill: var(--ink); letter-spacing: 3px; }
  .person-title { font-weight: 800; font-size: 22px; fill: var(--blue-deep); letter-spacing: 4px; }
</style>
</head>
<body>
<main class="canvas">

  <!-- Brand side -->
  <section class="card card--front">
    <svg viewBox="0 0 850 500" aria-label="Birchlane Furnishing brand side">
      <rect class="paper" width="850" height="500" fill="var(--paper)"/>
      <polygon class="shade-strip" points="150,170 175,175 420,500 392,500" fill="var(--shade)"/>
      <polygon class="panel-soft" points="0,0 70,0 390,500 0,500" fill="var(--blue-soft)"/>
      <polygon class="shade-band" points="680,300 850,35 850,58 700,305" fill="var(--shade)"/>
      <polygon class="band-ink" points="398,472 690,300 660,345 420,500 405,500" fill="var(--ink)"/>
      <polygon class="panel-deep" points="420,500 850,58 850,500" fill="var(--blue-deep)"/>
      <g class="brand-lockup">
        <rect x="275" y="232" width="20" height="20" fill="var(--blue-mid)"/>
        <text class="brand-name" x="305" y="252">BIRCHLANE FURNISHING</text>
        <text class="brand-tagline" x="306" y="276">TRADE FURNISHING SOLUTIONS</text>
      </g>
    </svg>
  </section>

  <!-- Details side -->
  <section class="card card--back">
    <svg viewBox="0 0 850 500" aria-label="Staff contact details">
      <defs>
        <linearGradient id="roomTone" x1="0" y1="0" x2="1" y2="1">
          <stop offset="0" stop-color="#9a9a9a"/>
          <stop offset="0.5" stop-color="#d8d8d6"/>
          <stop offset="1" stop-color="#8f8a82"/>
        </linearGradient>
      </defs>
      <rect width="850" height="500" fill="var(--paper)"/>
      <rect class="photo-area" x="0" y="0" width="590" height="500" fill="url(#roomTone)" role="img" aria-label="Photo of a furnished living room interior"/>
      <polygon class="panel-soft" points="20,340 550,90 480,400 290,400" fill="var(--blue-soft)"/>
      <polygon class="panel-deep" points="160,500 290,400 480,400 455,500" fill="var(--blue-deep)"/>
      <polygon class="paper-wedge" points="580,0 850,0 850,500 455,500" fill="var(--paper)"/>
      <polygon class="triangle-ink" points="570,60 770,405 495,340" fill="var(--ink)"/>
      <rect class="edge-bar" x="818" y="10" width="18" height="490" fill="var(--ink)"/>

      <!-- Company & address -->
      <g class="address-block" text-anchor="end">
        <text class="company-line" x="470" y="265">Birchlane Furnishing - Trade</text>
        <text class="address-line" x="470" y="289">27B Harrow Trade Park</text>
        <text class="address-line" x="470" y="311">Eastmere</text>
        <text class="address-line" x="470" y="333">London | E14 3QR</text>
      </g>
      <path class="icon-home" d="M480 257 l10 -9 l10 9 h-3 v8 h-5 v-5 h-4 v5 h-5 v-8 z" fill="var(--paper)"/>

      <!-- Web & email -->
      <g class="web-block" text-anchor="end">
        <text class="contact-line" x="440" y="440">www.birchlane.co.uk/</text>
        <text class="contact-line" x="440" y="464">hello@birchlane.co.uk</text>
      </g>
      <g class="icon-globe" fill="none" stroke="var(--paper)" stroke-width="2">
        <circle cx="455" cy="435" r="7"/>
        <ellipse cx="455" cy="435" rx="3" ry="7"/>
        <line x1="448" y1="435" x2="462" y2="435"/>
      </g>

      <!-- Phone numbers -->
      <g class="phone-block">
        <rect x="521" y="237" width="9" height="15" rx="1.5" fill="none" stroke="var(--paper)" stroke-width="2"/>
        <text class="contact-line" x="542" y="250">020 7946 0123</text>
        <path d="M518 270 q0 -4 3 -4 l2 4 -2 2 q2 4 5 5 l2 -2 4 2 q0 3 -4 3 q-10 -2 -10 -10z" fill="var(--paper)"/>
        <text class="contact-line" x="542" y="278">020 7946 0123</text>
        <g fill="var(--paper)">
          <rect x="514" y="292" width="10" height="5"/>
          <rect x="511" y="297" width="16" height="8" rx="1"/>
          <rect x="514" y="305" width="10" height="3"/>
        </g>
        <text class="contact-line" x="542" y="306">020 7946 0188</text>
      </g>

      <!-- Name & title -->
      <text class="person-name" x="505" y="448">DANIEL HART</text>
      <text class="person-title" x="530" y="480">-MANAGER-</text>
    </svg>
  </section>

</main>
</body>
</html>
```